Refresh Velmora Web Presence - www.velmora-example.com

Velmora (www.velmora-example.com)web site needs a makeover. It needs to be more modern, less cluttered, more corporate, prestigious, user friendly, impressive, up to date. We want a modern corporate image that encourages our business users to trust us and buy our products and services. They need to understand that they are dealing with a highly reputable, long established company, but one that is up to date and forward thinking.
1. Clean uncluttered design.
2. Domain Registration box and Countries (price) box to be collapsible and expandable.
3. All links on page need to be conserved for SEO but hidden from view.
4. Logo and general colour scheme need to be retained.
5. Phone number to be prominently displayed at top of page.
6. No calls to action (CTA) below the fold.
7. Sites we like: www.quibbleton-example.com, www.dealvane-example.com,www.nook-example.com,www.billtrove-example.com, www.saphilo-example.com (busy but clear CTAs), www.tervapoint-example.com
Updates
Project Deadline Extended
Reason: We lost a lot of time to review over the holiday weekend. We need to have a chance to interact during business hours.
Target Market(s)
Small business to large enterprise
Industry/Entity Type
Business
Look and feel
Each slider illustrates characteristics of the customer's brand and the style your logo design should communicate.

```html
<!DOCTYPE html>
<html lang="en">
<head>
<meta charset="utf-8">
<title>Velmora – Domain Names</title>
<link href="https://fonts.googleapis.com/css2?family=Play:wght@400;700&family=Oswald:wght@500;600&family=Open+Sans:wght@400;600;700&display=swap" rel="stylesheet">
<style>
:root{
  --navy:#2e3687;
  --navy-light:#4652b4;
  --orange:#e5650f;
  --orange-light:#f3922f;
  --ink:#333333;
  --grey-text:#555555;
  --sky:#dcebf7;
  --sky-deep:#b9d6ee;
  --white:#ffffff;
}
*{box-sizing:border-box;margin:0;padding:0}
html,body{width:1200px;height:1008px;overflow:hidden}
body{position:relative;background:#f6f6f6;font-family:"Open Sans",Arial,sans-serif;color:var(--ink)}
.abs{position:absolute}

/* top bar */
.topbar{left:0;top:0;width:1200px;height:41px;background:linear-gradient(#4651b0,var(--navy));color:var(--white);font-size:13px}
.topbar .chat{left:98px;top:12px;display:flex;align-items:center;gap:6px}
.whois{left:208px;top:9px;width:174px;height:22px;background:#e8ecf8;border-radius:3px;color:#777;font-size:12px;padding:3px 8px}
.whois .go{position:absolute;right:0;top:0;width:25px;height:22px;background:var(--orange);border-radius:0 3px 3px 0}
.phone{left:566px;top:6px;font-family:"Oswald",sans-serif;font-size:21px;font-weight:500;display:flex;align-items:center;gap:6px}
.toplinks{left:729px;top:12px;display:flex;gap:24px}
.login{left:1006px;top:0;width:84px;height:41px;background:var(--orange);font-size:15px;padding:11px 14px}

/* hero */
.hero{left:0;top:41px;width:1200px;height:462px;background:radial-gradient(ellipse at 45% 50%,#ffffff 0%,#eef5fb 45%,var(--sky) 75%,var(--sky-deep) 100%)}
.mapdeco{left:200px;top:100px;width:560px;height:370px;border-radius:40%;background:radial-gradient(ellipse,rgba(170,185,200,.35),rgba(170,185,200,0) 70%)}
.brand{left:100px;top:70px;display:flex;align-items:center;gap:10px;font-family:"Play",sans-serif;font-weight:700;font-size:40px;color:var(--navy)}
.brand .mark{width:44px;height:44px;border-radius:50%;background:var(--orange)}
.mainnav{left:0;top:89px;width:1200px;height:32px;font-weight:700;font-size:14.5px;color:#111}
.mainnav a{position:absolute;top:0;padding:5px 0;color:inherit;text-decoration:none;white-space:nowrap}
.mainnav a.on{background:var(--orange);color:var(--white);border-radius:4px;padding:5px 0;width:132px;text-align:center}
.mainnav a.on::after{content:"";position:absolute;left:50%;bottom:-6px;margin-left:-6px;border:6px solid transparent;border-bottom:0;border-top-color:var(--orange)}
.h-big{left:104px;top:168px;font-family:"Play",sans-serif;font-weight:700;font-size:66px;line-height:1;color:#333}
.h-big .num{color:var(--orange);font-size:86px}
.h-sub{left:104px;top:282px;font-family:"Play",sans-serif;font-weight:700;font-size:55px;color:#333;white-space:nowrap}
.h-acc{left:105px;top:359px;font-family:"Play",sans-serif;font-size:29px;letter-spacing:-.6px;color:var(--orange);white-space:nowrap}
.cta{left:104px;top:421px;width:284px;height:61px;border-radius:6px;background:linear-gradient(var(--orange-light),var(--orange));border:2px solid #fff;box-shadow:0 2px 4px rgba(0,0,0,.3);color:#fff;font-family:"Oswald",sans-serif;font-size:33px;font-weight:600;display:flex;align-items:center;padding-left:27px;gap:24px}
.cta-accent{left:410px;top:438px;width:132px;height:28px;border-radius:50%;background:radial-gradient(ellipse,rgba(217,52,43,.18),rgba(217,52,43,0) 70%)}
.boxart{left:725px;top:155px;width:370px;height:315px;border-radius:50%;background:radial-gradient(circle at 50% 45%,#e7a03a 0%,#d08a2c 28%,rgba(220,235,247,0) 60%)}
.dots{left:1025px;top:461px;display:flex;gap:4px}
.dots span{width:17px;height:17px;border-radius:50%;background:var(--navy-light);border:1px solid #fff}
.dots span:first-child{background:var(--orange-light)}

/* share bar */
.sharebar{left:0;top:503px;width:1200px;height:62px;background:linear-gradient(#f0f0f0,#d9d9d9);border-top:1px solid #c5c5c5}
.shares{left:100px;top:526px;display:flex;gap:10px;font-size:11px}
.share{display:flex;align-items:center}
.share .btn{display:flex;align-items:center;gap:4px;padding:1px 5px;border:1px solid #bbb;border-radius:2px;background:#f4f4f4;color:#334}
.share .btn i{width:9px;height:9px;border-radius:50%;background:#8a8fa8;display:block}
.share .cnt{margin-left:4px;border:1px solid #ccc;background:#fff;padding:1px 5px;color:#555}
.currency{left:724px;top:525px;font-family:"Play",sans-serif;font-weight:700;font-size:17px;color:#444}
.select{left:811px;top:517px;width:91px;height:35px;background:#fff;border:2px solid #cfcfcf;border-radius:4px;font-family:"Play",sans-serif;font-weight:700;font-size:17px;padding:5px 12px}
.country{left:920px;top:517px;width:168px;height:35px;border-radius:4px;background:linear-gradient(var(--orange-light),var(--orange));color:#fff;font-family:"Play",sans-serif;font-weight:700;font-size:16px;padding:6px 16px}

/* tabs */
.tabs{left:0;top:594px;width:1200px;height:40px;font-family:"Play",sans-serif;font-weight:700;font-size:21px;color:#555}
.tabs span{position:absolute;top:0;padding:6px 0 8px;white-space:nowrap}
.tabs span.on{background:linear-gradient(#e4e4e4,#f6f6f6);border-radius:8px 8px 0 0;padding:6px 14px 8px}
.www{left:97px;top:680px;font-family:"Play",sans-serif;font-weight:700;font-size:32px;color:var(--navy)}
.searchbox{left:204px;top:669px;width:640px;height:65px;background:#fff;border:2px solid #cfcfcf;border-radius:5px 0 0 5px;font-size:33px;color:#aaa;padding:9px 22px}
.searchbtn{left:814px;top:669px;width:273px;height:65px;background:linear-gradient(var(--orange-light),var(--orange));clip-path:polygon(24px 0,100% 0,100% 100%,24px 100%,0 50%);border-radius:0 6px 6px 0;color:#fff;font-family:"Oswald",sans-serif;font-weight:600;font-size:38px;padding:5px 0 0 58px;display:flex;gap:22px}

/* extensions panel */
.panel{left:97px;top:778px;width:991px;height:195px;background:#fff;border:2px solid #d4d4d4;border-radius:5px}
.regions{left:99px;top:780px;width:987px;height:43px;background:var(--navy);font-family:"Play",sans-serif;font-weight:700;font-size:17px;color:#fff}
.regions label{position:absolute;top:10px;display:flex;align-items:center;gap:9px}
.cb{width:20px;height:20px;border:1px solid #b5b5b5;background:#fff;display:inline-block;position:relative}
.cb.on svg{position:absolute;left:1px;top:-6px}
.pointer{left:121px;top:822px;width:116px;height:13px;background:var(--navy);clip-path:polygon(0 0,100% 0,50% 100%)}
.ext{position:absolute;display:flex;align-items:center;gap:10px;font-size:15px;color:#444}
.more{left:495px;top:956px;width:199px;height:30px;background:#fff;border:2px solid #d4d4d4;border-radius:14px;color:var(--orange);font-weight:600;font-size:13px;text-align:center;padding-top:5px}
</style>
</head>
<body>
<header class="abs topbar">
  <div class="abs chat"><svg width="16" height="13" viewBox="0 0 16 13"><ellipse cx="8" cy="5.5" rx="7.5" ry="5" fill="#fff"/><path d="M3 9 L2 13 L7 10Z" fill="#fff"/></svg>Chat with us</div>
  <div class="abs whois">Whois Seach<span class="go"><svg width="25" height="22" viewBox="0 0 25 22"><circle cx="14" cy="9" r="4" fill="none" stroke="#fff" stroke-width="2"/><path d="M11 12 L7 16" stroke="#fff" stroke-width="2.5"/></svg></span></div>
  <div class="abs phone"><svg width="10" height="16" viewBox="0 0 10 16"><rect x="1" y="1" width="8" height="14" rx="2" fill="#fff"/><rect x="3" y="3" width="4" height="6" fill="#4651b0"/></svg>+1.5550148823</div>
  <nav class="abs toplinks"><span>Register</span><span>Shopping Cart</span><span>View Cart (0)</span></nav>
  <div class="abs login">Login <svg width="14" height="10" viewBox="0 0 14 10"><path d="M1 2 L7 8 L13 2Z" fill="#fff"/></svg></div>
</header>

<section class="abs hero"></section>
<div class="abs mapdeco" role="img" aria-label="Faint dotted world map behind the headline"></div>
<div class="abs brand"><span class="mark"></span>Velmora</div>
<nav class="abs mainnav">
  <a class="on" style="left:373px">Domain Names</a>
  <a style="left:512px">IDN Domains</a>
  <a style="left:627px">New gTLDs</a>
  <a style="left:725px">Phone Numbers</a>
  <a style="left:862px">Hosting</a>
  <a style="left:938px">Resellers</a>
  <a style="left:1023px">About Us</a>
</nav>
<h1 class="abs h-big"><span class="num">300</span>+ DOMAIN</h1>
<div class="abs h-sub">NAME EXTENSIONS</div>
<div class="abs h-acc">ACCREDITED IN OVER 100 COUNTRIES</div>
<div class="abs cta">VIEW PRICING <svg width="26" height="30" viewBox="0 0 26 30"><path d="M0 2 L12 15 L0 28Z M12 2 L24 15 L12 28Z" fill="#fff"/></svg></div>
<div class="abs cta-accent" role="img" aria-label="Hand-drawn red arrow pointing at the pricing button"></div>
<div class="abs boxart" role="img" aria-label="Open cardboard box surrounded by a ring of colourful domain extensions"></div>
<div class="abs dots"><span></span><span></span><span></span></div>

<section class="abs sharebar"></section>
<div class="abs shares">
  <div class="share"><span class="btn"><i></i>Share</span><span class="cnt">18</span></div>
  <div class="share"><span class="btn"><i></i>Like</span><span class="cnt">3k</span></div>
  <div class="share"><span class="btn"><i></i>Post</span><span class="cnt">11.9K</span></div>
</div>
<div class="abs currency">Currency</div>
<div class="abs select">USD <svg style="position:absolute;right:10px;top:13px" width="14" height="8" viewBox="0 0 14 8"><path d="M0 0 L7 8 L14 0Z" fill="#e5650f"/></svg></div>
<div class="abs country">Select Country <svg width="14" height="9" viewBox="0 0 14 9"><path d="M0 0 L7 9 L14 0Z" fill="#fff"/></svg></div>

<nav class="abs tabs">
  <span class="on" style="left:97px">Domain Registration</span>
  <span style="left:361px">IDN</span>
  <span style="left:440px">Bulk Search</span>
  <span style="left:602px">Transfer</span>
  <span style="left:728px">Renew</span>
  <span style="left:836px">Map Search</span>
  <span style="left:994px">PhNUM</span>
</nav>
<div class="abs www">www.</div>
<div class="abs searchbox">Search for a new domain</div>
<div class="abs searchbtn">SEARCH <svg width="38" height="40" viewBox="0 0 38 40"><circle cx="15" cy="15" r="11" fill="none" stroke="#fff" stroke-width="4"/><path d="M23 24 L34 36" stroke="#fff" stroke-width="6" stroke-linecap="round"/></svg></div>

<section class="abs panel"></section>
<div class="abs regions">
  <label style="left:24px"><span class="cb"></span>Generic</label>
  <label style="left:158px"><span class="cb"></span>Europe</label>
  <label style="left:286px"><span class="cb on"><svg width="24" height="24" viewBox="0 0 24 24"><path d="M3 13 L9 20 L22 2" fill="none" stroke="#2e3687" stroke-width="3"/></svg></span>Asia/Pacific</label>
  <label style="left:450px"><span class="cb"></span>America</label>
  <label style="left:587px"><span class="cb"></span>Africa</label>
  <label style="left:719px"><span class="cb"></span>All Domains</label>
</div>
<div class="abs pointer"></div>

<div class="ext" style="left:134px;top:859px"><span class="cb"></span>.biz</div>
<div class="ext" style="left:241px;top:859px"><span class="cb"></span>.co</div>
<div class="ext" style="left:352px;top:859px"><span class="cb on"><svg width="24" height="24" viewBox="0 0 24 24"><path d="M3 13 L9 20 L22 2" fill="none" stroke="#2e3687" stroke-width="3"/></svg></span>.com</div>
<div class="ext" style="left:466px;top:859px"><span class="cb"></span>.info</div>
<div class="ext" style="left:573px;top:859px"><span class="cb"></span>.mobi</div>
<div class="ext" style="left:684px;top:859px"><span class="cb on"><svg width="24" height="24" viewBox="0 0 24 24"><path d="M3 13 L9 20 L22 2" fill="none" stroke="#2e3687" stroke-width="3"/></svg></span>.name</div>
<div class="ext" style="left:794px;top:859px"><span class="cb"></span>.net</div>
<div class="ext" style="left:878px;top:859px"><span class="cb"></span>.me</div>
<div class="ext" style="left:964px;top:859px"><span class="cb"></span>.org</div>
<div class="ext" style="left:134px;top:910px"><span class="cb"></span>.pro</div>
<div class="ext" style="left:241px;top:910px;font-size:13px"><span class="cb"></span>.pty-ltd.com</div>
<div class="ext" style="left:352px;top:910px"><span class="cb on"><svg width="24" height="24" viewBox="0 0 24 24"><path d="M3 13 L9 20 L22 2" fill="none" stroke="#2e3687" stroke-width="3"/></svg></span>.tel</div>
<div class="ext" style="left:466px;top:910px"><span class="cb"></span>.travel</div>
<div class="ext" style="left:573px;top:910px"><span class="cb"></span>.xxx</div>

<div class="abs more">Show More Extensions <svg width="14" height="10" viewBox="0 0 14 10"><path d="M0 0 L7 6 L14 0Z M0 4 L7 10 L14 4Z" fill="#e5650f"/></svg></div>
</body>
</html>
```